Valtimore Sciences needs high end Label Design for a revolutionary new supplement

We at Valtimore Sciences are looking for a brand new Label Design for a first of its kind product called Tolmisse. It is the first supplement on the market that treats grief and heartbreak. This product is unisex for both men and woman. We want the New Label to look high end and luxurious using the brand colors which are gold and burgundy. Please feel free to use other colors such as black, white, or gray to go along with it or any other colors if you feel would be a great fit! Valtimore Sciences is like the Quorvel of the supplement world, coming out with new products that will challenge the way people treat different symptoms. To Recap:

1. Product Name: TOLMISSE - the font will play a big roll
2. The Label will be placed on an all white bottle
3. Some parts of the label will be printed with foil to make parts of the label shiny and more attractive. Please keep this in mind when designing.
4. Must use our Logo. I will attach a file of our logo and of the emblem as well. Feel free to use the emblem separately if you have a great idea for it. Please let us know if you need the Logo in a different file type.
5. This all natural herbal supplement in pill form is the first to treat grief and support someone with a broken heart. The consumers purchasing this product will be going through a hard and emotional time. This is a serious product.
6. The manufacturer has included some basic instructions regarding the dye line and file types. Please do your best to meet these. If you cannot meet the guidelines please submit art work anyways. If your design is chosen we will just have the manufacturer replicate the design.

The final label should portray Tolmisse and Valtimore Sciences as a luxurious brand and product which was made with cutting edge science leading the way with revolutionary ideas. We want customers to feel that the product is worth every penny, because it is. As soon as they receive the product and take one look at the label, I want them to think WOW I made the right choice buying this. I have attached some Label designs that we really liked for your review.

Please feel free to message me with any questions or if you need the Logo in a different file type. Thank you all.
Updates

Please send in more entries while we take a couple days to review, we are still looking for that one design we can work with. We are getting close, thank you all!

Target Market(s)

People going through grief and heartbreak.

Font styles to use
Sans Serif
Script
Other font styles liked:
• Any font that looks good, The font for the name TOLMISSE is very important and will brand it. We hated the font used in the label we received in our first label draft (attached so you can see)

Requirements
Must have
• Must have the company Logo that says the company name
• Must have the colors Gold and Burgundy
• Must have some areas that will be the shiny foil when label is printed.
• Must say "Dietary Supplement" somewhere near the bottom along with "90 Capsules"
• I have attached a Label someone designed for us but were not really happy with. I did like the font the "Dietary supplement" and "90 Capsules" had and also where it was placed. We absolutely HATED the font used for Tolmisse.
• Must look at the label design we received from the manufacturer and take into consideration the room needed to write in the directions and all the symbols such as "made in america" and "BQH Facility" Don't worry about adding these in as they will put those in before printing but keep in mind they will be added to the Final Label along with the Supplement Facts.
Nice to have
• Would like to see other colors to go with gold and burgundy suck as black, white, or gray. I have attached some Label designs that I really liked for your reference.
Should not have
• Does not need to have any other legal language, that will be applied by the the manufacturer's graphics team.

```html
<!DOCTYPE html>
<html lang="en">
<head>
<meta charset="utf-8">
<title>Tolmisse Label – Valtimore Sciences</title>
<link rel="stylesheet" href="https://fonts.googleapis.com/css2?family=Alfa+Slab+One&family=Cinzel:wght@500&family=Cormorant+Garamond:wght@500&family=Raleway:wght@500;800&display=swap">
<style>
  :root {
    --burgundy: #4a0003;
    --burgundy-deep: #2a0001;
    --burgundy-glow: #5c0206;
    --gold: #c9a36b;
    --gold-light: #f3e3c4;
    --gold-dark: #8a5a2b;
    --ink: #0b0b0b;
  }
  * { margin: 0; padding: 0; box-sizing: border-box; }
  html, body { width: 1200px; height: 830px; overflow: hidden; background: var(--burgundy-deep); }
  .label {
    position: relative;
    width: 1200px;
    height: 830px;
    background: radial-gradient(ellipse 70% 80% at 50% 50%, var(--burgundy-glow) 0%, var(--burgundy) 55%, var(--burgundy-deep) 100%);
    overflow: hidden;
  }
  .foil-band {
    position: absolute;
    left: 0;
    width: 100%;
    height: 26px;
    background: linear-gradient(90deg, var(--gold-dark) 0%, var(--gold) 25%, var(--gold-light) 50%, var(--gold) 75%, var(--gold-dark) 100%);
  }
  .foil-band--top { top: 13px; }
  .foil-band--bottom { top: 788px; }
  .brand {
    position: absolute;
    top: 66px;
    left: 0;
    width: 100%;
    text-align: center;
    color: var(--gold);
    font-family: "Cinzel", serif;
    font-weight: 500;
  }
  .brand__mark {
    display: block;
    width: 96px;
    height: 96px;
    margin: 0 auto 26px;
    border: 3px solid var(--gold);
    border-radius: 50%;
    transform: translateX(-6px);
  }
  .brand__name {
    display: block;
    font-size: 42px;
    letter-spacing: 5px;
    line-height: 46px;
    transform: translateX(-6px);
  }
  .brand__name--second { font-size: 34px; letter-spacing: 7px; }
  .product-name {
    position: absolute;
    top: 330px;
    left: 190px;
    width: 810px;
    height: 140px;
  }
  .product-name text {
    font-family: "Alfa Slab One", serif;
    font-size: 136px;
  }
  .count {
    position: absolute;
    top: 592px;
    left: 0;
    width: 100%;
    text-align: center;
    transform: translateX(-6px);
  }
  .count__number {
    display: block;
    font-family: "Cormorant Garamond", serif;
    font-weight: 500;
    font-size: 92px;
    line-height: 86px;
    color: var(--gold-light);
  }
  .count__unit {
    display: block;
    font-family: "Raleway", sans-serif;
    font-weight: 500;
    font-size: 19px;
    letter-spacing: 1px;
    color: var(--gold);
  }
  .rule {
    position: absolute;
    left: 412px;
    width: 364px;
    height: 1px;
    background: var(--gold);
    opacity: 0.7;
  }
  .rule--upper { top: 708px; }
  .rule--lower { top: 766px; }
  .category {
    position: absolute;
    top: 724px;
    left: 0;
    width: 100%;
    text-align: center;
    font-family: "Raleway", sans-serif;
    font-weight: 800;
    font-size: 23px;
    letter-spacing: 1px;
    color: var(--gold);
    transform: translateX(-6px);
  }
</style>
</head>
<body>
  <main class="label">
    <div class="foil-band foil-band--top"></div>

    <header class="brand">
      <span class="brand__mark"></span>
      <span class="brand__name">VALTIMORE</span>
      <span class="brand__name brand__name--second">SCIENCES</span>
    </header>

    <svg class="product-name" viewBox="0 0 810 140" aria-label="Tolmisse">
      <defs>
        <linearGradient id="foil-gold" x1="0" y1="0" x2="1" y2="0">
          <stop offset="0" stop-color="#a8743f"/>
          <stop offset="0.3" stop-color="#e8cfa6"/>
          <stop offset="0.55" stop-color="#fbf1dd"/>
          <stop offset="0.8" stop-color="#d7b27f"/>
          <stop offset="1" stop-color="#a8743f"/>
        </linearGradient>
      </defs>
      <text x="10" y="122" textLength="790" lengthAdjust="spacingAndGlyphs"
            fill="var(--ink)" stroke="url(#foil-gold)" stroke-width="14"
            stroke-linejoin="miter" paint-order="stroke fill">TOLMISSE</text>
    </svg>

    <div class="count">
      <span class="count__number">90</span>
      <span class="count__unit">CAPSULES</span>
    </div>
    <div class="rule rule--upper"></div>
    <p class="category">DIETARY SUPPLEMENT</p>
    <div class="rule rule--lower"></div>

    <div class="foil-band foil-band--bottom"></div>
  </main>
</body>
</html>
```